Fishing charter business in Sitka Alaska needs new business card design

I have had the same design for 10 plus years, ready for something different. I have attached a copy of my current card and my website link is www.bluecoveangling.net
I am looking for something that will catch my clients eye, although I rely on word of mouth for most of my business a a nice business card will help people remember who I am. My business is located in Sitka Alaska, there are probably 20-30 other charter businesses in Sitka. I like the way my current card is laid out, with the two tone black and grey. I can leave it up to the designers to come up with something else.
Target Market(s)
men, women, couples. Anyone who likes fishing
Industry/Entity Type
Tourism
Contact Information for Business Card
Dorrance's Charter Service
Tidewater Rockline Sportfishing
Colors
Designer to choose colors to be used in the design.
Requirements
Must have
- Gilbert Dorrance
- PO Box 4716
- Sitka, AK 99835
- Compass Rose image
- 100 Ton USCG Licensed Captain
- gdorrance@wavelink.net
- 907-555-0142
- www.bluecoveangling.net
Nice to have
- ghost image of "boat helm"
Should not have
- be to complex

```html
<!DOCTYPE html>
<html lang="en">
<head>
<meta charset="utf-8">
<title>Gilbert Dorrance – Business Card</title>
<link href="https://fonts.googleapis.com/css2?family=Belleza&family=Marcellus&display=swap" rel="stylesheet">
<style>
  :root {
    --backdrop: #272727;
    --card: #ffffff;
    --ink: #141414;
    --ink-soft: #2c2c2c;
    --rule: #3a3a3a;
    --compass-dark: #5a5a5a;
    --compass-light: #f1f1f1;
  }
  * { margin: 0; padding: 0; box-sizing: border-box; }
  html, body {
    width: 1200px;
    height: 895px;
    overflow: hidden;
    background: var(--backdrop);
  }
  .stage {
    width: 1200px;
    height: 895px;
    display: flex;
    align-items: center;
    justify-content: center;
  }
  .business-card {
    position: relative;
    width: 980px;
    height: 560px;
    background: var(--card);
    border-radius: 42px;
    font-family: "Belleza", "Optima", sans-serif;
    color: var(--ink);
  }
  .compass-art {
    position: absolute;
    left: 130px;
    top: 120px;
    width: 320px;
    height: 320px;
  }
  .details {
    position: absolute;
    left: 500px;
    top: 150px;
  }
  .name {
    font-family: "Marcellus", "Optima", serif;
    font-weight: 400;
    font-size: 38px;
    letter-spacing: 0.5px;
    line-height: 1;
    color: var(--ink);
    text-shadow: 0.6px 0 0 var(--ink);
    white-space: nowrap;
  }
  .title {
    font-size: 19px;
    margin-top: 6px;
    color: var(--ink-soft);
    letter-spacing: 0.3px;
  }
  .contact-block {
    position: relative;
    margin-top: 46px;
    margin-left: 44px;
    padding-left: 30px;
  }
  .contact-block::before {
    content: "";
    position: absolute;
    left: 0;
    top: 20px;
    width: 1.5px;
    height: 62px;
    background: var(--rule);
  }
  .contact-list { list-style: none; }
  .contact-item {
    display: flex;
    align-items: center;
    gap: 14px;
    font-size: 19px;
    line-height: 28px;
    color: var(--ink-soft);
    white-space: nowrap;
  }
  .contact-icon { width: 13px; height: 13px; flex: none; }
  .address {
    margin-top: 34px;
    margin-left: 74px;
    font-size: 19px;
    color: var(--ink-soft);
    letter-spacing: 0.3px;
    white-space: nowrap;
  }
</style>
</head>
<body>
<main class="stage">
  <section class="business-card">
    <svg class="compass-art" viewBox="0 0 320 320" role="img" aria-label="Hand-drawn compass rose illustration with N, E, S, W points and a faint ghost compass behind">
      <defs>
        <radialGradient id="compassTone" cx="50%" cy="50%" r="50%">
          <stop offset="0%" stop-color="#5a5a5a"/>
          <stop offset="45%" stop-color="#9a9a9a"/>
          <stop offset="100%" stop-color="#f1f1f1"/>
        </radialGradient>
      </defs>
      <circle cx="160" cy="160" r="150" fill="url(#compassTone)"/>
    </svg>

    <div class="details">
      <h1 class="name">GILBERT DORRANCE</h1>
      <p class="title">100 Ton USCG Licensed Captain</p>

      <div class="contact-block">
        <ul class="contact-list">
          <li class="contact-item">
            <svg class="contact-icon" viewBox="0 0 16 16" aria-hidden="true"><path d="M4 1.5 6.2 4.3 4.8 6a9 9 0 0 0 5.2 5.2l1.7-1.4 2.8 2.2-1.6 2.5C7 14 2 9 1.5 3.1Z" fill="#141414"/></svg>
            <span>907-555-0142</span>
          </li>
          <li class="contact-item">
            <svg class="contact-icon" viewBox="0 0 16 16" aria-hidden="true"><rect x="1" y="3" width="14" height="10" rx="1" fill="#141414"/><path d="M1.5 3.8 8 9l6.5-5.2" fill="none" stroke="#fff" stroke-width="1.3"/></svg>
            <span>gdorrance@wavelink.net</span>
          </li>
          <li class="contact-item">
            <svg class="contact-icon" viewBox="0 0 16 16" aria-hidden="true"><circle cx="8" cy="8" r="7" fill="#141414"/><path d="M1 8h14M8 1v14M3 4.2h10M3 11.8h10" stroke="#fff" stroke-width="0.9" fill="none"/><ellipse cx="8" cy="8" rx="3.2" ry="7" fill="none" stroke="#fff" stroke-width="0.9"/></svg>
            <span>www.bluecoveangling.net</span>
          </li>
        </ul>
      </div>

      <p class="address">PO Box 4716 - Sitka, AK 99835</p>
    </div>
  </section>
</main>
</body>
</html>
```